PowerPoint template for Credit Card Processor

We need a powerpoint template for our new credit card processing company. Our goal is to sign up merchants to accept credit cards. We will be making presentations to merchants to get them to sign up for our services.

We already have a logo designed. We'd like to incorporate that logo and color scheme in the powerpoint template. The logo file is an illustrator file.

I generally like light colored backgrounds. Nothing too dark.

Industry/Entity Type

Credit Card

Requirements
Must have
• our logo

```html
<!DOCTYPE html>
<html lang="en">
<head>
<meta charset="utf-8">
<title>FlowGate.net – Presentation Template</title>
<link href="https://fonts.googleapis.com/css2?family=Oswald:wght@400;600&family=Pathway+Gothic+One&family=Open+Sans:wght@400;600;700&display=swap" rel="stylesheet">
<style>
  :root {
    --frame: #2b2a29;
    --paper: #ffffff;
    --paper-cool: #e9eef3;
    --brand: #1e8fcb;
    --brand-deep: #2c7cb3;
    --brand-soft: #3a92c9;
    --cyan: #2ec3f0;
    --ink: #4a4a4a;
    --ink-soft: #666666;
    --rule: #c9ced3;
    --footer: #4b4b4b;
    --chart-grey: #7f7f80;
    --chart-cyan: #41b4e4;
    --pie-blue: #0f8fd1;
    --pie-purple: #8a3fcf;
    --pie-green: #12a46c;
    --pie-orange: #d9800f;
    --social-1: #7ccbef;
    --social-2: #2f86c8;
    --social-3: #1f72b2;
    --display: "Oswald", "Arial Narrow", sans-serif;
    --narrow: "Pathway Gothic One", "Arial Narrow", sans-serif;
    --body: "Open Sans", Arial, sans-serif;
  }
  * { box-sizing: border-box; margin: 0; padding: 0; }
  html, body { width: 1060px; height: 1200px; overflow: hidden; }
  body { background: var(--frame); position: relative; font-family: var(--body); color: var(--ink); }

  .slide { position: absolute; width: 514px; height: 385px; background: var(--paper); overflow: hidden; }
  .col-a { left: 12px; } .col-b { left: 533px; }
  .row-1 { top: 9px; } .row-2 { top: 405px; } .row-3 { top: 802px; }

  .brand { position: absolute; display: flex; align-items: center; font-family: var(--narrow); color: var(--ink); white-space: nowrap; }
  .brand-dot { border-radius: 50%; background: var(--cyan); flex: none; }
  .brand--hero { font-size: 56px; gap: 16px; }
  .brand--hero .brand-dot { width: 46px; height: 46px; }
  .brand--small { font-size: 15px; gap: 5px; }
  .brand--small .brand-dot { width: 10px; height: 10px; }
  .brand--light { color: #fff; }
  .brand--light .brand-dot { background: #fff; }

  /* Title slide */
  .cover-photo { position: absolute; inset: 0; background: linear-gradient(120deg, #dfe6ed 0%, #eef2f6 55%, #e4eaf0 100%); }
  .title-block { position: absolute; left: 102px; top: 123px; width: 412px; height: 139px; background: var(--brand-soft); text-align: right; padding: 22px 20px 0 0; }
  .title-block h1 { font-family: var(--display); font-weight: 400; color: #fff; font-size: 50px; line-height: 1; letter-spacing: 0.5px; white-space: nowrap; }
  .title-block p { font-family: var(--narrow); color: var(--cyan); font-size: 27px; line-height: 1.2; margin-top: 4px; }
  .cover-meta { position: absolute; right: 18px; top: 278px; text-align: right; font-family: var(--narrow); }
  .cover-meta .kind { font-size: 19px; color: var(--ink); }
  .cover-meta .date { font-size: 15px; color: var(--brand); margin-top: 2px; }

  /* Agenda */
  .agenda-rail { position: absolute; left: 0; top: 0; width: 114px; height: 100%; background: var(--brand); }
  .agenda-rail .rail-title { position: absolute; left: 10px; top: 351px; font-family: var(--narrow); color: #fff; font-size: 15px; line-height: 1; white-space: nowrap; }
  .agenda-rail .rail-sub { position: absolute; left: 10px; width: 94px; text-align: center; top: 369px; font-family: var(--narrow); color: #9fdcf5; font-size: 8px; line-height: 1; white-space: nowrap; }
  .agenda-heading { position: absolute; left: 131px; top: 52px; font-family: var(--display); font-weight: 600; color: var(--brand); font-size: 27px; letter-spacing: 0.3px; }
  .agenda-item { position: absolute; left: 131px; width: 383px; height: 24px; }
  .agenda-item .topic { position: absolute; left: 2px; top: 0; font-family: var(--narrow); font-size: 18px; color: var(--ink-soft); }
  .agenda-item .topic-line { position: absolute; left: 0; bottom: 0; width: 361px; border-bottom: 1px solid var(--rule); }
  .agenda-item .page { position: absolute; right: 6px; top: 3px; font-size: 11px; color: var(--brand); }
  .agenda-item .page-line { position: absolute; right: 0; bottom: 0; width: 24px; border-bottom: 1px solid var(--brand); }

  /* Content slides */
  .title-band { position: absolute; left: 0; top: 0; width: 100%; height: 38px; background: var(--brand); }
  .title-band h2 { font-family: var(--body); font-weight: 400; font-size: 23px; color: #fff; line-height: 38px; padding-left: 8px; letter-spacing: 0.2px; }
  .slide-footer { position: absolute; left: 0; bottom: 0; width: 100%; height: 22px; background: var(--footer); display: flex; align-items: center; font-size: 9px; color: #fff; }
  .slide-footer .num { width: 25px; height: 100%; background: var(--brand); display: flex; align-items: center; justify-content: center; font-size: 10px; }
  .slide-footer .brand { position: static; margin-left: 10px; font-size: 14px; }
  .slide-footer .sep { margin: 0 6px; opacity: 0.8; }
  .slide-footer .sub { color: var(--cyan); font-size: 7px; margin-left: 8px; }

  .image-slot { position: absolute; left: 26px; top: 72px; width: 222px; height: 258px; background: linear-gradient(180deg, #3b93cb 0%, #2c7cb3 100%); }
  .image-slot svg { position: absolute; left: 73px; top: 92px; }

  .bullets { position: absolute; list-style: none; font-size: 8.6px; line-height: 1.36; color: var(--ink); text-align: justify; }
  .bullets li { position: relative; padding-left: 13px; margin-bottom: 9px; }
  .bullets li::before { content: ""; position: absolute; left: 1px; top: 4px; width: 7px; height: 3px; border-radius: 2px; background: var(--brand); }
  .bullets li.sub { margin-left: 30px; }
  .bullets li.sub::before { background: var(--cyan); }
  .bullets b { font-weight: 700; }
  .bullets--content { left: 267px; top: 63px; width: 221px; }
  .bullets--chart { width: 195px; font-size: 6.8px; line-height: 1.35; text-align: left; }
  .bullets--chart li { margin-bottom: 10px; }
  .bullets--chart li::before { top: 3px; width: 6px; height: 2.5px; }

  .chart-title { position: absolute; top: 80px; font-size: 14.5px; color: var(--ink); }
  .chart-title b { font-weight: 700; }
  .area-chart { position: absolute; left: 20px; top: 95px; }
  .pie-chart { position: absolute; left: 303px; top: 102px; }
  .chart-label { font-family: var(--body); font-size: 7px; fill: var(--ink); }
  .pie-label { font-family: var(--body); font-size: 12px; fill: #fff; }

  /* Closing */
  .contact { position: absolute; left: 15px; font-size: 6.8px; line-height: 1.35; color: var(--ink); }
  .contact h3 { font-size: 8.6px; font-weight: 700; }
  .social { position: absolute; top: 366px; width: 18px; height: 18px; }
</style>
</head>
<body>

<!-- Opening brand slide -->
<section class="slide col-a row-1 slide--brand">
  <div class="brand brand--hero" style="left:92px; top:157px;"><span class="brand-dot"></span>FlowGate.net</div>
</section>

<!-- Title slide -->
<section class="slide col-b row-1 slide--title">
  <div class="cover-photo" role="img" aria-label="Faint close-up photograph of a circuit board in pale blue-grey tones"></div>
  <div class="brand brand--small" style="right:14px; top:102px;"><span class="brand-dot"></span>FlowGate.net</div>
  <div class="title-block">
    <h1>PRESENTATION TITLE</h1>
    <p>Presentation Subtitle</p>
  </div>
  <div class="cover-meta">
    <div class="kind">Company Presentation</div>
    <div class="date">September 2013</div>
  </div>
</section>

<!-- Agenda slide -->
<section class="slide col-a row-2 slide--agenda">
  <aside class="agenda-rail">
    <div class="brand brand--small brand--light" style="left:13px; top:26px;"><span class="brand-dot"></span>FlowGate.net</div>
    <div class="rail-title">PRESENTATION TITLE</div>
    <div class="rail-sub">Presentation Subtitle</div>
  </aside>
  <h2 class="agenda-heading">TODAY’S AGENDA</h2>
  <div class="agenda-item" style="top:96px;"><span class="topic">Presentation Topic Title</span><span class="topic-line"></span><span class="page">#</span><span class="page-line"></span></div>
  <div class="agenda-item" style="top:143px;"><span class="topic">Presentation Topic Title</span><span class="topic-line"></span><span class="page">#</span><span class="page-line"></span></div>
  <div class="agenda-item" style="top:195px;"><span class="topic">Presentation Topic Title</span><span class="topic-line"></span><span class="page">#</span><span class="page-line"></span></div>
  <div class="agenda-item" style="top:245px;"><span class="topic">Presentation Topic Title</span><span class="topic-line"></span><span class="page">#</span><span class="page-line"></span></div>
  <div class="agenda-item" style="top:304px;"><span class="topic">Presentation Topic Title</span><span class="topic-line"></span><span class="page">#</span><span class="page-line"></span></div>
</section>

<!-- Content slide: image and bullets -->
<section class="slide col-b row-2 slide--content">
  <header class="title-band"><h2>PRESENTATION SLIDE TITLE</h2></header>
  <div class="image-slot" role="img" aria-label="Image placeholder area">
    <svg width="76" height="76" viewBox="0 0 76 76" aria-hidden="true">
      <rect x="2" y="2" width="72" height="72" fill="none" stroke="#4fa3d6" stroke-width="4"/>
      <circle cx="22" cy="24" r="7" fill="#4fa3d6"/>
      <path d="M10 64 L30 36 L40 50 L52 32 L68 64 Z" fill="#4fa3d6"/>
    </svg>
  </div>
  <ul class="bullets bullets--content">
    <li><b>Aenean</b> ridiculus tortor quis interdum id habitant ad, natoque consectetuer nisl auctor libero quisque euismod ante inceptos malesuada ligula mattis.</li>
    <li class="sub">Nulla, netus pulvinar pellentesque porttitor purus maecenas tellus hac nulla lacus. Lorem. Nostra laoreet nulla, dis cursus nascetur dolor odio Eu Magna molestie montes dui mus cursus habitasse mauris tempor.</li>
    <li class="sub">Varius inceptos <b>nascetur</b> mollis dui aptent ultrices. Pretium pulvinar ante lobortis convallis lectus netus vitae penatibus eros at blandit. Parturient.</li>
    <li><b>Aenean</b> ridiculus tortor quis interdum id habitant ad, natoque consectetuer nisl auctor libero quisque euismod ante inceptos malesuada ligula mattis.</li>
  </ul>
  <footer class="slide-footer">
    <span class="num">4</span>
    <span class="brand brand--small brand--light"><span class="brand-dot"></span>FlowGate.net</span>
    <span class="sep">|</span>PRESENTATION TITLE<span class="sub">Presentation Subtitle</span>
  </footer>
</section>

<!-- Content slide: charts -->
<section class="slide col-a row-3 slide--charts">
  <header class="title-band"><h2>PRESENTATION SLIDE TITLE</h2></header>

  <div class="chart-title" style="left:36px;"><b>Graph</b> Main Colors</div>
  <svg class="area-chart" width="240" height="165" viewBox="0 0 240 165" role="img" aria-label="Area chart, 2007 to 2010">
    <g stroke="#d7d9dc" stroke-width="0.8">
      <line x1="30" y1="8" x2="220" y2="8"/>
      <line x1="30" y1="42" x2="220" y2="42"/>
      <line x1="30" y1="76" x2="220" y2="76"/>
      <line x1="30" y1="111" x2="220" y2="111"/>
      <line x1="30" y1="145" x2="220" y2="145"/>
    </g>
    <g text-anchor="end">
      <text x="24" y="10" class="chart-label">100</text>
      <text x="24" y="44" class="chart-label">75</text>
      <text x="24" y="78" class="chart-label">50</text>
      <text x="24" y="113" class="chart-label">25</text>
      <text x="24" y="147" class="chart-label">0</text>
    </g>
    <path d="M30 74 L93 88 L157 51 L220 62 L220 145 L30 145 Z" fill="var(--chart-grey)"/>
    <path d="M30 104 L93 118 L157 100 L220 110 L220 145 L30 145 Z" fill="var(--chart-cyan)"/>
    <path d="M30 121 L93 108 L157 71 L220 11 L220 145 L30 145 Z" fill="var(--brand-deep)"/>
    <g text-anchor="middle">
      <text x="30" y="155" class="chart-label">2007</text>
      <text x="93" y="155" class="chart-label">2008</text>
      <text x="157" y="155" class="chart-label">2009</text>
      <text x="220" y="155" class="chart-label">2010</text>
    </g>
  </svg>

  <div class="chart-title" style="left:303px;"><b>Graph</b> Secondary Colors</div>
  <svg class="pie-chart" width="150" height="150" viewBox="-75 -75 150 150" role="img" aria-label="Pie chart: 50%, 28%, 14%, 9%">
    <path d="M0 0 L0 -73 A73 73 0 0 1 39.1 -61.6 Z" fill="var(--pie-purple)"/>
    <path d="M0 0 L39.1 -61.6 A73 73 0 0 1 72.4 -9.2 Z" fill="var(--pie-green)"/>
    <path d="M0 0 L72.4 -9.2 A73 73 0 0 1 -4.6 72.9 Z" fill="var(--pie-orange)"/>
    <path d="M0 0 L-4.6 72.9 A73 73 0 0 1 0 -73 Z" fill="var(--pie-blue)"/>
    <text x="13" y="-43" class="pie-label">9%</text>
    <text x="28" y="-17" class="pie-label">14%</text>
    <text x="25" y="40" class="pie-label">28%</text>
    <text x="-63" y="14" class="pie-label">50%</text>
  </svg>

  <ul class="bullets bullets--chart" style="left:34px; top:265px;">
    <li><b>Aenean</b> ridiculus tortor quis interdum id habitant ad, natoque consectetuer nisl auctor libero quisque euismod ante inceptos malesuada ligula mattis.</li>
    <li>Varius inceptos <b>nascetur</b> mollis dui aptent ultrices. Pretium pulvinar ante lobortis convallis lectus netus vitae penatibus eros at blandit. Parturient.</li>
  </ul>
  <ul class="bullets bullets--chart" style="left:287px; top:265px; width:210px;">
    <li><b>Aenean</b> ridiculus tortor quis interdum id habitant ad, natoque consectetuer nisl auctor libero quisque euismod ante inceptos malesuada ligula mattis.</li>
    <li>Varius inceptos <b>nascetur</b> mollis dui aptent ultrices. Pretium pulvinar ante lobortis convallis lectus netus vitae penatibus eros at blandit. Parturient.</li>
  </ul>

  <footer class="slide-footer">
    <span class="num">5</span>
    <span class="brand brand--small brand--light"><span class="brand-dot"></span>FlowGate.net</span>
    <span class="sep">|</span>PRESENTATION TITLE<span class="sub">Presentation Subtitle</span>
  </footer>
</section>

<!-- Closing slide -->
<section class="slide col-b row-3 slide--closing">
  <div class="brand brand--hero" style="left:74px; top:167px;"><span class="brand-dot"></span>FlowGate.net</div>
  <div class="contact" style="top:301px;">
    <h3>Contact us:</h3>
    <div>888-888-8888</div>
    <div>sales@flowgate.net</div>
  </div>
  <div class="contact" style="top:346px;">
    <h3>Our Office</h3>
    <div>Address Line 1</div>
    <div>Address Line 2</div>
  </div>
  <span class="social" style="left:430px; background:var(--social-1);"></span>
  <span class="social" style="left:458px; background:var(--social-2);"></span>
  <span class="social" style="left:485px; background:var(--social-3);"></span>
</section>

</body>
</html>
```